E-Book-Cover Wo Schatten tanzen
Zielgruppe
Der Titel ist: Wo Schatten tanzen
Der Autorenname ist: Helga Brommert
Dies ist der letzte Teil einer Trilogie. Es geht um Wiebke. Sie leidet an einer Angststörung, nachdem sie von ihrem Ex-Mann misshandelt wurde. Doch sie traut sich nicht ihren Lebensgefährten und Psychologen Anselm einzuweihen. Die beiden streiten sich häufig und trennen sich schließlich. Aber sie können nicht mit- und auch nicht ohne einander. Schließlich schafft sie es Anselm von ihrem Geheimnis zu erzählen. Ihr Ex-Mann hat eine Bank überfallen, weshalb er schließlich verhaftet wurde und sie ihn los war.
Parallelgeschichte dazu ist: Ilka ist schwanger. Bela und sie freuen sich riesig darüber und erklären Anselm und Freundin Greta zu Patentante und -onkel.
Aufgabenstellung
Ich brauche das Cover mit einer Mindestbreite von 1600 Pixel. Es soll den Zwiespalt der Gefühle ausdrücken, den Wiebke und Anselm haben. Man soll natürlich auch eine Verbindung zu den anderen beiden Covern erkennen (s. angehangene Bilder). Da die ersten beiden Cover schwarz-weiß sind, würde ich es gern beim dritten Cover so beibehalten. Die Schriftart sollte auch wieder in die gleiche Richtung gehen. Es dürfen gern Menschen auf dem Cover zu sehen sein, müssen aber nicht, wenn die gleiche Stimmung erzeugt wird.

```html
<!DOCTYPE html>
<html lang="de">
<head>
<meta charset="utf-8">
<title>Wo Schatten tanzen – Helga Brommert</title>
<link rel="stylesheet" href="https://fonts.googleapis.com/css2?family=Montserrat:wght@400;500&family=Dancing+Script:wght@500;600&display=swap">
<style>
  :root {
    --stage: #f2f2f2;
    --cover-dark: #121212;
    --cover-deep: #1c1c1c;
    --cover-mid: #3a3a3a;
    --skin-light: #cfcfcf;
    --skin-mid: #9a9a9a;
    --key-white: #e8e8e8;
    --ink-light: #ffffff;
    --ink-soft: #ececec;
  }
  * { box-sizing: border-box; margin: 0; padding: 0; }
  html, body {
    width: 1200px;
    height: 844px;
    overflow: hidden;
    background: var(--stage);
  }
  .canvas {
    width: 1200px;
    height: 844px;
    display: flex;
    justify-content: center;
    align-items: center;
    gap: 60px;
  }
  .cover {
    position: relative;
    width: 467px;
    height: 700px;
    background: var(--cover-dark);
    overflow: hidden;
    box-shadow: 0 14px 30px rgba(0,0,0,0.22);
  }
  .cover-photo {
    position: absolute;
    inset: 0;
    background:
      /* bright key strip under the hands */
      radial-gradient(ellipse 22% 5% at 48% 57%, rgba(232,232,232,0.85), transparent 75%),
      /* upper hand, light diagonal band */
      linear-gradient(152deg, transparent 26%, rgba(207,207,207,0.0) 27%, rgba(207,207,207,0.55) 33%, rgba(170,170,170,0.45) 41%, transparent 48%),
      /* lower hand, softer band */
      linear-gradient(168deg, transparent 44%, rgba(154,154,154,0.35) 49%, rgba(120,120,120,0.25) 54%, transparent 59%),
      /* instrument body, dark rounded mass on the right */
      radial-gradient(ellipse 45% 40% at 85% 30%, rgba(70,70,70,0.7), transparent 70%),
      radial-gradient(ellipse 30% 12% at 62% 50%, rgba(10,10,10,0.6), transparent 80%),
      linear-gradient(180deg, var(--cover-mid) 0%, #2a2a2a 30%, var(--cover-deep) 65%, var(--cover-dark) 100%);
  }
  .cover-back .cover-photo {
    background:
      radial-gradient(ellipse 20% 5% at 48% 58%, rgba(232,232,232,0.7), transparent 75%),
      linear-gradient(158deg, transparent 30%, rgba(200,200,200,0.4) 38%, rgba(160,160,160,0.35) 46%, transparent 54%),
      linear-gradient(170deg, transparent 46%, rgba(140,140,140,0.25) 52%, transparent 60%),
      radial-gradient(ellipse 45% 35% at 80% 18%, rgba(75,75,75,0.7), transparent 70%),
      linear-gradient(180deg, #2e2e2e 0%, #222 35%, var(--cover-deep) 65%, var(--cover-dark) 100%);
  }
  .author-name {
    position: absolute;
    top: 32px;
    left: 0;
    right: 0;
    text-align: center;
    font-family: "Montserrat", sans-serif;
    font-weight: 500;
    font-size: 21px;
    letter-spacing: 0.14em;
    color: var(--ink-light);
  }
  .front-title {
    position: absolute;
    top: 365px;
    left: 16px;
    right: 16px;
    text-align: center;
    font-family: "Dancing Script", cursive;
    font-weight: 600;
    font-size: 86px;
    line-height: 1.12;
    color: var(--ink-light);
  }
  .back-title {
    position: absolute;
    top: 72px;
    left: 0;
    right: 0;
    text-align: center;
    font-family: "Dancing Script", cursive;
    font-weight: 600;
    font-size: 44px;
    color: var(--ink-light);
  }
  .blurb {
    position: absolute;
    top: 158px;
    left: 26px;
    right: 26px;
    font-family: "Montserrat", sans-serif;
    font-size: 13.6px;
    line-height: 1.76;
    text-align: justify;
    color: var(--ink-soft);
  }
</style>
</head>
<body>
  <main class="canvas">
    <section class="cover cover-front">
      <div class="cover-photo" role="img" aria-label="Schwarz-weißes Foto: zwei Hände von zwei Menschen übereinander auf den Tasten eines Flügels"></div>
      <p class="author-name">Helga Brommert</p>
      <h1 class="front-title">Wo Schatten<br>tanzen</h1>
    </section>

    <section class="cover cover-back">
      <div class="cover-photo" role="img" aria-label="Schwarz-weißes Foto: Hände auf den Tasten eines Flügels, abgedunkelt"></div>
      <h2 class="back-title">Wo Schatten tanzen</h2>
      <div class="blurb">
        <p>Dies ist der letzte Teil einer Trilogie. Es geht um Wiebke. Sie leidet an einer Angststörung, nachdem sie von ihrem Ex-Mann misshandelt wurde. Doch sie traut sich nicht ihren Lebensgefährten und Psychologen Anselm einzuweihen. Die beiden streiten sich häufig und trennen sich schließlich. Aber sie können nicht mit- und auch nicht ohne einander. Schließlich schafft sie es Anselm von ihrem Geheimnis zu erzählen. Ihr Ex-Mann hat eine Bank überfallen, weshalb er schließlich verhaftet wurde und sie ihn los war.</p>
        <p>Parallelgeschichte dazu ist: Ilka ist schwanger. Bela und sie freuen sich riesig darüber und erklären Anselm und Freundin Greta zu Patentante und -onkel.</p>
      </div>
    </section>
  </main>
</body>
</html>
```